Sticker label design for - Tidal Fern Deodorant Balm

I need a label for my 100% Natural Deodorant Balm
The brand is called "Plum Meadow Brand", and the product is called TIDAL FERN Deodorant Balm.
There are two labels, one is a 5.2cm circle for the top, and 4.5cm circle for the base. The jar is amber plastic with black lid.
Width: 5.8cm
Height: 3.4cm (Lid 1.2cm, base 2,2cm)
Here is a link to what the jar looks like from one of my competitors: https://copperwren.com.au/products/body/velaro-deodorant-paste/
The product is a unisex product. Please see uploaded files for designs previously made for the brand. I'm trying to see a few more designs before finalising my choice. Feel free to use the logo at the top (Plum Meadow Brand) of either attachment if you would like. Or design your own.
Be be aware that it is meant to be Aluminium and Paraben Free, not "Parabens" Weight of product is 70g, please include this.
Label can be any colour, and printed with regular colours or event gold, silver or rose gold foil. Would a background be nice?
This is something I saw that I liked:
http://www.mossvelbalm.com
However I'm really open to what people can come up with.
For the back base-
Tidal Fern deodorant balm is made from 100% natural ingredients, and works by neutralises odour and minimising wetness without the use of harmful chemicals.
www.plummeadowbrand.com
Directions: For optimal result, apply a pea size amount of the balm to your dry armpits. Gently rub the balm into your armpits covering the entire area. Discontinue use if irritation occurs.
Ingredients: Shea Butter, Coconut oil, Sodium Bicarbonate, Arrowroot, Kaolin Clay, Vitamin E, Vegetable Glycerin, Activated Charcoal, Essential oils of Peppermint, Lavender, Mandarin, Tea tree, Geranium Rose & Cedarwood.
MADE IN AUSTRALIA
Reason: Hi,
I'm not getting many submissions, so was hoping to extend the deadline.
Skin Care Product

```html
<!DOCTYPE html>
<html lang="en">
<head>
<meta charset="utf-8">
<title>Tidal Fern Deodorant Balm – Jar Labels</title>
<link href="https://fonts.googleapis.com/css2?family=Libre+Baskerville:wght@400;700&family=Encode+Sans+Condensed:wght@300;400;500;700&family=Arimo:wght@400&display=swap" rel="stylesheet">
<style>
  :root {
    --canvas: #f2f2f2;
    --label-green: #c3cc8b;
    --shadow-green: #8e9a5a;
    --ink: #151515;
    --earth: #8a7042;
  }
  * { margin: 0; padding: 0; box-sizing: border-box; }
  html, body { width: 1200px; height: 1200px; overflow: hidden; background: var(--canvas); }
  .sheet { position: relative; width: 1200px; height: 1200px; }

  .lid-label {
    position: absolute; left: 355px; top: 127px;
    width: 490px; height: 490px; border-radius: 50%;
    overflow: hidden; background: var(--label-green);
  }
  .lid-label .fold { position: absolute; left: 0; top: 0; }
  .brand-name {
    position: absolute; left: 0; right: 0; top: 100px;
    text-align: center; font-family: "Libre Baskerville", serif;
    font-size: 27px; line-height: 36px; color: var(--earth);
  }
  .product-name {
    position: absolute; left: 0; right: 0; top: 238px; text-align: center;
    font-family: "Libre Baskerville", serif; font-weight: 700;
    font-size: 41px; letter-spacing: 0.5px; color: var(--ink);
  }
  .product-type {
    position: absolute; left: 0; right: 0; top: 296px; text-align: center;
    font-family: "Encode Sans Condensed", sans-serif; font-weight: 500;
    font-size: 25px; letter-spacing: 1.5px; color: var(--ink);
  }
  .rule {
    position: absolute; left: 141px; width: 200px; top: 345px;
    height: 2px; background: var(--ink);
  }
  .claims {
    position: absolute; left: 0; right: 0; top: 358px; text-align: center;
    font-family: "Arimo", sans-serif; font-size: 19px; line-height: 25px;
    color: var(--earth);
  }
  .net-weight {
    position: absolute; left: 0; right: 0; top: 438px; text-align: center;
    font-family: "Encode Sans Condensed", sans-serif; font-weight: 500;
    font-size: 15px; color: var(--ink);
  }

  .base-label {
    position: absolute; left: 416px; top: 706px;
    width: 368px; height: 368px; border-radius: 50%;
    background: var(--label-green); text-align: center;
    font-family: "Encode Sans Condensed", sans-serif; font-weight: 300;
    color: var(--ink); font-size: 13.5px; line-height: 20px;
  }
  .base-label p { position: absolute; left: 0; right: 0; }
  .about { top: 24px; }
  .website { top: 109px; color: var(--earth); font-weight: 400; }
  .directions { top: 136px; }
  .ingredients { top: 201px; }
  .ingredients strong { font-weight: 700; }
  .origin { top: 322px; color: var(--earth); font-size: 12px; }
</style>
</head>
<body>
<main class="sheet">
  <section class="lid-label">
    <svg class="fold" width="490" height="490" viewBox="0 0 490 490" aria-hidden="true">
      <defs>
        <linearGradient id="foldShadow" x1="0" y1="0" x2="0" y2="1">
          <stop offset="0" stop-color="var(--shadow-green)" stop-opacity="0.85"/>
          <stop offset="1" stop-color="var(--label-green)" stop-opacity="0"/>
        </linearGradient>
      </defs>
      <polygon points="45,102 245,215 445,100 490,100 490,230 245,300 0,230 0,102" fill="url(#foldShadow)"/>
      <polygon points="0,0 490,0 490,100 445,100 245,215 45,102 0,102" fill="var(--label-green)"/>
    </svg>
    <p class="brand-name">Plum Meadow<br>Brand</p>
    <h1 class="product-name">TIDAL FERN</h1>
    <p class="product-type">DEODORANT BALM</p>
    <div class="rule"></div>
    <p class="claims">100% Natural |Aluminum &amp;<br>Paraben Free | Vegan | Cruelty Free</p>
    <p class="net-weight">NET WT. 2.4 OZ &#8494; 70gms</p>
  </section>

  <section class="base-label">
    <p class="about">Tidal Fern deodorant balm is<br>made from 100% natural ingredients,<br>and works by neutralises odour and minimising<br>wetness without the use of harmful chemicals.</p>
    <p class="website">www.plummeadowbrand.com</p>
    <p class="directions">Directions: For optimal result, apply a pea size amount<br>of the balm to your dry armpits. Gently rub the balm into your<br>armpits covering the entire area. Discontinue use if irritation occurs.</p>
    <p class="ingredients"><strong>INGREDIENTS</strong>: Shea Butter, Coconut oil, Sodium Bicarbonate,<br>Arrowroot, Kaolin Clay, Vitamin E, Vegetable Glycerin,<br>Activated Charcoal, Essential oils of Peppermint,<br>Lavender, Mandarin, Tea tree, Geranium<br>Rose &amp; Cedarwood.</p>
    <p class="origin">MADE IN AUSTRALIA</p>
  </section>
</main>
</body>
</html>
```